New Stationery New Logo for KT Fabrication Limited

We have a new logo and now want new stationary to go with it

This will be

Letterhead
Compliments Slip
Business Cards

Company details are
KT Fabrication Limited
Dellmoor Road, Rugby, Warwickshire, CV34 7HX, UK
Telephone : +44(0)1788 390617
Fax: +44(0)1788 473928
Email: sales@ktfabrication.co.uk
Web: www.ktfabrication.co.uk

Target Market(s)

Engineering / Metal Stamping

Industry/Entity Type

Manufacture

Contact Information for Business Card

Colin Brearley
Business Development Manager
KT Fabrication Limited
Dellmoor Road
Rugby
Warwickshire
CV34 7HX, UK

T: +44(0)1788 390617
F: +44(0)1788 473928
E: sales@ktfabrication.co.uk
W: www.ktfabrication.co.uk

Font styles to use
Sans Serif

Colors
33a6d7
0555a3
3176b5
85cae6
85acd3

Requirements
Must have
• Logo

```html
<!DOCTYPE html>
<html lang="en">
<head>
<meta charset="utf-8">
<title>KT Fabrication Stationery</title>
<link href="https://fonts.googleapis.com/css2?family=Lato:ital,wght@0,400;0,700;1,300&display=swap" rel="stylesheet">
<style>
  :root {
    --bg: #dcdddf;
    --paper: #ffffff;
    --brand: #134d96;
    --brand-dark: #1a3e8c;
    --ink: #111111;
    --script: #3f67b1;
    --faint: #f3f3f3;
  }
  * { box-sizing: border-box; margin: 0; padding: 0; }
  html, body { width: 1200px; height: 2308px; overflow: hidden; }
  body { background: var(--bg); font-family: "Lato", sans-serif; color: var(--ink); position: relative; }

  .sheet { position: absolute; background: var(--paper); box-shadow: 0 2px 6px rgba(0,0,0,.18); overflow: hidden; }
  .letterhead { left: 118px; top: 58px; width: 965px; height: 1363px; }
  .compliments { left: 118px; top: 1482px; width: 965px; height: 454px; }

  .brand-name { position: absolute; color: var(--brand); font-weight: 400; letter-spacing: .26em; white-space: nowrap; display: flex; align-items: center; gap: 12px; }
  .brand-name .dot { width: 14px; height: 14px; border-radius: 50%; background: var(--brand); display: inline-block; }
  .sheet .brand-name { left: 48px; top: 138px; font-size: 25px; }

  .company { position: absolute; left: 561px; top: 72px; font-size: 12px; line-height: 17px; font-weight: 700; }
  .company .title { font-size: 13px; }
  .contacts { position: absolute; left: 757px; top: 72px; font-size: 12px; line-height: 17px; font-weight: 700; }
  .contacts b { color: var(--brand); }

  .band { position: absolute; left: 0; right: 0; bottom: 0; background: var(--brand); color: #fff; font-weight: 700; font-size: 16px; display: flex; align-items: center; justify-content: center; }
  .letterhead .band { height: 48px; }
  .compliments .band { height: 46px; }
  .band .corner-name { position: absolute; right: 28px; font-weight: 700; font-size: 13px; letter-spacing: .18em; }

  .watermark { position: absolute; left: 0; right: 0; top: 620px; text-align: center; color: var(--faint); font-size: 96px; font-weight: 700; letter-spacing: .1em; }

  .compliments .company { top: 58px; left: 571px; }
  .compliments .contacts { top: 58px; left: 771px; }
  .compliments .brand-name { top: 122px; left: 36px; }
  .with-compliments { position: absolute; left: 37px; top: 345px; font-size: 30px; font-style: italic; font-weight: 300; color: var(--script); }

  .card { position: absolute; top: 1995px; width: 392px; height: 252px; background: var(--paper); border-radius: 15px; box-shadow: 0 2px 6px rgba(0,0,0,.18); overflow: hidden; }
  .card-front { left: 194px; }
  .card-back { left: 615px; }
  .card .person { position: absolute; left: 25px; top: 40px; }
  .person .name { font-size: 18px; font-weight: 700; color: var(--brand-dark); }
  .person .role { font-size: 10px; font-weight: 700; letter-spacing: .03em; }
  .card .details { position: absolute; left: 25px; top: 84px; font-size: 11px; line-height: 16px; font-weight: 700; }
  .details b { color: var(--brand); }
  .card-front .brand-name { left: 25px; top: 172px; font-size: 19px; gap: 9px; }
  .card-front .brand-name .dot { width: 11px; height: 11px; }
  .card-front .band { height: 38px; justify-content: flex-start; padding-left: 27px; font-size: 15px; }
  .card-back .brand-name { left: 0; right: 0; top: 150px; justify-content: center; font-size: 22px; }
</style>
</head>
<body>

<section class="sheet letterhead">
  <div class="brand-name">KT FABRICATION <span class="dot"></span></div>
  <div class="company">
    <div class="title">KT Fabrication Limited</div>
    <div>Dellmoor Road, Rugby</div>
    <div>Warwickshire, CV34 7HX, UK</div>
  </div>
  <div class="contacts">
    <div><b>T:</b> +44(0)1788 390617</div>
    <div><b>F:</b> +44(0)1788 473928</div>
    <div><b>E:</b> sales@ktfabrication.co.uk</div>
  </div>
  <div class="watermark">KT FABRICATION</div>
  <footer class="band">www.ktfabrication.co.uk<span class="corner-name">KT FABRICATION</span></footer>
</section>

<section class="sheet compliments">
  <div class="brand-name">KT FABRICATION <span class="dot"></span></div>
  <div class="company">
    <div class="title">KT Fabrication Limited</div>
    <div>Dellmoor Road, Rugby</div>
    <div>Warwickshire, CV34 7HX, UK</div>
  </div>
  <div class="contacts">
    <div><b>T:</b> +44(0)1788 390617</div>
    <div><b>F:</b> +44(0)1788 473928</div>
    <div><b>E:</b> sales@ktfabrication.co.uk</div>
  </div>
  <div class="with-compliments">with compliments</div>
  <footer class="band">www.ktfabrication.co.uk<span class="corner-name">KT FABRICATION</span></footer>
</section>

<section class="card card-front">
  <div class="person">
    <div class="name">COLIN BREARLEY</div>
    <div class="role">MANAGER</div>
  </div>
  <div class="details">
    <div>Dellmoor Road, Rugby, Warwickshire, CV34 7HX, UK</div>
    <div><b>T:</b> +44(0)1788 390617</div>
    <div><b>F:</b> +44(0)1788 473928</div>
    <div><b>E:</b> colin@ktfabrication.co.uk</div>
  </div>
  <div class="brand-name">KT FABRICATION <span class="dot"></span></div>
  <footer class="band">www.ktfabrication.co.uk</footer>
</section>

<section class="card card-back">
  <div class="brand-name">KT FABRICATION <span class="dot"></span></div>
</section>

</body>
</html>
```